Heavy Equipment Rental Company Looking for Attractive Sign Design

We need a new sign for our forklift rental company in Southern California called Ridgeline Lift Partners. We also sell, service and move forklifts and other equipment, but forklift rentals are our main business. Our old sign on the street is deteriorating quickly. I've attached a photo of the old sign - it is approximately 52" high and 48" wide, but may be made 6" or so taller if needed. The old sign is included more to reference the information than the design - the old design definitely has issues (no SketchHive at the time). The smaller sign reading Borvex dealer is not needed. We want the sign to be simple, clean and easy to read, but of course also attractive and professional. We would like the same information on it as is on the previous sign, but it may be re-arranged. The number 4815 is the street number. Here are the essential elements:
4815 (street number)
Ridgeline Lift Partners (business name)
714-382-0476 (phone)
www.ridgelinelifts-example.com (website)
Forklift Rentals and Sales (main businesses)
If possible, we would like the names of our 2 primary brands:
Borvex and Tavilo Forklifts
Although, if there's no way to implement them nicely, then we can leave them off.

Target Market(s)

Industrial, Construction

Industry/Entity Type

Construction

Colors
0355a3

Requirements
Must have
• Bold, clean, easy to read, with the necessary information.
Nice to have
• Our main machines are all painted blue, so some blue in the design would be nice. In our industry, Borvex forklifts and Tavilo forklifts are two different brands but have good reputations. It would be nice if we can include them in the design, although a nice design is more important than including the brand names.
Should not have
• Small or difficult to read text. Colors or fonts that are too playful.

```html
<!DOCTYPE html>
<html lang="en">
<head>
<meta charset="utf-8">
<title>Ridgeline Lift Partners — Street Sign</title>
<link rel="stylesheet" href="https://fonts.googleapis.com/css2?family=Jost:wght@500;600;700&display=swap">
<style>
  :root {
    --sign-blue: #0b55a3;
    --frame-yellow: #ffc20e;
    --accent-orange: #f58220;
    --sign-white: #ffffff;
    --backdrop: #e9eaec;
  }
  html, body {
    margin: 0;
    width: 1200px;
    height: 1200px;
    overflow: hidden;
    background: var(--backdrop);
  }
  .canvas {
    position: relative;
    width: 1200px;
    height: 1200px;
    display: flex;
    align-items: center;
    justify-content: center;
  }
  .street-sign {
    width: 836px;
    height: 1131px;
    display: block;
  }
  .sign-text {
    font-family: "Jost", "Futura", sans-serif;
    font-weight: 700;
  }
  .street-number, .business-name, .services-line { fill: var(--sign-white); }
  .tagline, .phone-number, .website { fill: var(--sign-blue); }
  .website { font-weight: 600; }
</style>
</head>
<body>
<main class="canvas">
  <svg class="street-sign" viewBox="0 0 950 1285" xmlns="http://www.w3.org/2000/svg" aria-label="Ridgeline Lift Partners street sign">
    <defs>
      <linearGradient id="rimGradient" gradientUnits="userSpaceOnUse" x1="0" y1="0" x2="950" y2="0">
        <stop offset="0" stop-color="#f58220"/>
        <stop offset="0.75" stop-color="#ffd200"/>
        <stop offset="1" stop-color="#f58220"/>
      </linearGradient>
      <linearGradient id="frameGradient" gradientUnits="userSpaceOnUse" x1="0" y1="0" x2="950" y2="0">
        <stop offset="0" stop-color="#ffd200"/>
        <stop offset="1" stop-color="#f7941d"/>
      </linearGradient>
      <radialGradient id="iconGradient" cx="0.4" cy="0.35" r="0.7">
        <stop offset="0" stop-color="#fbb040"/>
        <stop offset="1" stop-color="#f15a24"/>
      </radialGradient>
    </defs>

    <path class="panel-white" d="M0,52 Q430,-22 950,80 V1275 H0 Z" fill="var(--sign-white)"/>
    <path class="panel-blue" d="M0,52 Q430,-22 950,80 V775 Q560,880 0,725 Z" fill="var(--sign-blue)"/>
    <path class="panel-rim" d="M0,725 Q560,880 950,775" fill="none" stroke="url(#rimGradient)" stroke-width="7"/>

    <g class="inner-frame" fill="none" stroke="url(#frameGradient)" stroke-width="4">
      <path d="M40,737 V80 Q470,20 908,100 V772"/>
      <line x1="40" y1="233" x2="255" y2="233"/>
      <line x1="692" y1="233" x2="908" y2="233"/>
    </g>

    <text class="sign-text street-number" x="475" y="275" font-size="152" text-anchor="middle" textLength="355" lengthAdjust="spacingAndGlyphs">4815</text>
    <text class="sign-text business-name" x="93" y="420" font-size="110" textLength="767" lengthAdjust="spacingAndGlyphs">RIDGELINE</text>
    <text class="sign-text business-name" x="476" y="592" font-size="204" text-anchor="middle" textLength="600" lengthAdjust="spacing">LIFT</text>
    <text class="sign-text services-line" x="93" y="697" font-size="104" textLength="767" lengthAdjust="spacing">PARTNERS</text>

    <text class="sign-text tagline" x="88" y="938" font-size="58" textLength="774" lengthAdjust="spacingAndGlyphs">FORKLIFT RENTALS AND SALES</text>

    <g class="icon-phone">
      <circle cx="135" cy="1045" r="35" fill="url(#iconGradient)"/>
      <circle cx="135" cy="1045" r="24" fill="none" stroke="#ffffff" stroke-width="3"/>
      <path d="M125,1031 l6,8 -4,4 q3,7 10,11 l4,-4 8,6 -4,6 q-18,-2 -26,-26 z" fill="#ffffff"/>
    </g>
    <text class="sign-text phone-number" x="203" y="1080" font-size="108" font-weight="600" textLength="657" lengthAdjust="spacingAndGlyphs">714-382-0476</text>

    <g class="icon-web">
      <circle cx="135" cy="1160" r="35" fill="url(#iconGradient)"/>
      <g fill="none" stroke="#ffffff" stroke-width="3">
        <circle cx="135" cy="1160" r="23"/>
        <ellipse cx="135" cy="1160" rx="10" ry="23"/>
        <line x1="112" y1="1160" x2="158" y2="1160"/>
        <line x1="116" y1="1148" x2="154" y2="1148"/>
        <line x1="116" y1="1172" x2="154" y2="1172"/>
        <line x1="135" y1="1137" x2="135" y2="1183"/>
      </g>
    </g>
    <text class="sign-text website" x="197" y="1178" font-size="46" textLength="663" lengthAdjust="spacingAndGlyphs">www.ridgelinelifts-example.com</text>
  </svg>
</main>
</body>
</html>
```